Website of KESTRAVO | The Amber Horizon Company

I need a simple and effective website where users can quickly understand what the company is all about and the added value of the services provided. The site should be attractive and modern, based on the logo and on the corporate slideshow attached.

Target Market(s)

Public and Private organizations from maritime security and defense, looking for solutions in the field s of digital transformation and cybersecurity.

Coding

Coded - Design and coding required

Requirements
Must have
• A form through which can contact the company by email to request additional information.

```html
<!DOCTYPE html>
<html lang="en">
<head>
<meta charset="utf-8">
<title>KESTRAVO | The Amber Horizon Company</title>
<link href="https://fonts.googleapis.com/css2?family=Montserrat:wght@400;500;600;700;800&display=swap" rel="stylesheet">
<style>
:root{
  --navy:#0a2536;
  --deep:#0d3245;
  --teal:#12445a;
  --cyan:#17a3d8;
  --ink:#0b1f2c;
  --muted:#4a5a66;
  --light:#f1f3f5;
  --white:#ffffff;
  --sky:#2d9fd6;
}
*{margin:0;padding:0;box-sizing:border-box}
html,body{width:1200px;height:3252px;overflow:hidden;background:var(--white);font-family:"Montserrat",sans-serif;color:var(--ink)}
.page{position:relative;width:1200px;height:3252px}
.brand{display:flex;align-items:center;gap:10px}
.brand-mark{width:22px;height:22px;background:var(--cyan);border-radius:4px}
.brand-name{font-weight:800;font-size:20px;color:var(--navy);letter-spacing:1px}
.brand-sub{font-size:8px;color:var(--cyan);letter-spacing:1px;margin-top:-2px}
/* header */
.site-header{position:absolute;top:0;left:0;width:1200px;height:40px;display:flex;justify-content:space-between;align-items:center;padding:0 44px}
.nav{display:flex;gap:22px;align-items:center;font-size:9px;font-weight:600}
.nav a{color:var(--ink);text-decoration:none}
.nav a.active{color:var(--cyan)}
.nav .dot{width:18px;height:18px;border-radius:50%;background:var(--navy)}
/* hero */
.hero{position:absolute;top:40px;left:0;width:1200px;height:380px}
.hero-photo{position:absolute;left:0;top:0;width:820px;height:380px;border-radius:0 0 0 90px;background:linear-gradient(135deg,#2e6f8c 0%,#1c4d66 40%,#0d3245 100%)}
.hero-panel{position:absolute;left:640px;top:0;width:560px;height:380px;background:var(--navy);border-radius:170px 0 0 170px;padding:70px 60px 0 90px}
.hero-panel h1{color:var(--cyan);font-size:36px;font-weight:800;line-height:1.12;text-transform:uppercase}
.hero-panel p{color:var(--white);font-size:13px;font-weight:600;margin-top:16px;line-height:1.4}
.hero-panel .tag{color:var(--cyan);font-size:10px;font-weight:600;margin-top:18px}
/* about */
.about{position:absolute;top:420px;left:0;width:1200px;height:600px}
.about-text{position:absolute;left:200px;top:240px;width:400px}
h2.section{font-size:28px;font-weight:800;color:var(--cyan);text-transform:uppercase}
.about-text p{font-size:10px;line-height:1.55;color:var(--muted);margin-top:14px}
.btn{display:inline-block;background:var(--ink);color:var(--white);font-size:9px;font-weight:700;padding:8px 16px;border-radius:4px;margin-top:20px;text-transform:uppercase}
.about-photo{position:absolute;left:700px;top:210px;width:300px;height:360px;border-radius:20px 150px 150px 20px;background:linear-gradient(160deg,#5f7f95,#2c4a5e 60%,#1a3244)}
/* services */
.services{position:absolute;top:1020px;left:0;width:1200px;height:1000px;background:linear-gradient(180deg,var(--deep),var(--navy));border-radius:180px 0 180px 0;color:var(--white)}
.services h2.section{position:absolute;top:55px;width:100%;text-align:center}
.svc-photo{position:absolute;left:190px;top:135px;width:380px;height:330px;border-radius:50%;background:radial-gradient(circle at 40% 40%,#4c6677,#1c3446 70%)}
.strategy{position:absolute;left:630px;top:140px;width:380px}
.strategy h3,.exec h3{color:var(--cyan);font-size:17px;font-weight:800;text-transform:uppercase}
.strategy>p,.exec>p{font-size:9px;color:#9fb4c2;margin-top:6px;line-height:1.5}
.item{display:flex;gap:12px;margin-top:22px}
.ico{flex:none;width:34px;height:34px;border-radius:50%;background:var(--cyan);display:flex;align-items:center;justify-content:center}
.item h4{color:var(--cyan);font-size:11px;font-weight:700}
.item p{font-size:9px;line-height:1.5;color:#d5e1e8;margin-top:3px}
.exec{position:absolute;left:0;top:560px;width:1200px;text-align:center}
.exec>p{width:560px;margin:6px auto 0}
.steps{display:flex;justify-content:center;gap:36px;margin-top:36px}
.step{width:170px;text-align:center}
.step .ico{width:48px;height:48px;margin:0 auto;background:var(--white)}
.step h4{color:var(--cyan);font-size:11px;font-weight:700;margin-top:10px}
.step p{font-size:9px;line-height:1.5;color:#d5e1e8;margin-top:4px}
.exec .btn{background:var(--white);color:var(--ink);margin-top:34px}
/* why */
.why{position:absolute;top:2020px;left:0;width:1200px;height:520px}
.why h2.section{position:absolute;top:105px;width:100%;text-align:center;color:var(--ink)}
.why-text{position:absolute;left:200px;top:195px;width:420px}
.why-text h3{color:var(--cyan);font-size:16px;font-weight:800;text-transform:uppercase}
.why-text .lead{font-size:10px;line-height:1.55;color:var(--muted);margin-top:6px}
.why-text h4{color:var(--cyan);font-size:10px;font-weight:700;margin-top:16px}
.why-text p.small{font-size:9px;line-height:1.5;color:var(--muted);margin-top:2px}
.why-photo{position:absolute;left:640px;top:170px;width:360px;height:330px;border-radius:20px 165px 165px 20px;background:radial-gradient(circle at 45% 50%,#2aa7e0,#0e3c60 55%,#071726)}
/* collaborate */
.collab{position:absolute;top:2540px;left:0;width:1200px;height:500px;background:var(--light)}
.collab h2.section{position:absolute;top:70px;width:100%;text-align:center}
.collab-photo{position:absolute;left:195px;top:140px;width:330px;height:330px;border-radius:50%;background:linear-gradient(170deg,#b7c9d6,#6f8798 55%,#3b5466)}
.form{position:absolute;left:610px;top:155px;width:400px}
.form h3{font-size:14px;font-weight:800;text-transform:uppercase}
.form>p{font-size:9px;line-height:1.5;color:var(--muted);margin-top:8px}
.form .row{display:flex;gap:10px;margin-top:10px}
.field{flex:1;height:26px;background:var(--white);border:1px solid #d6dde2;border-radius:4px;font-size:8px;color:#9aa6ae;padding:8px 10px}
.field.tall{height:60px;margin-top:10px}
.form .btn{margin-top:14px}
/* footer */
.site-footer{position:absolute;top:3000px;left:0;width:1200px;height:252px;background:var(--navy);border-radius:120px 0 0 0;color:var(--white)}
.site-footer .brand{position:absolute;left:200px;top:60px}
.site-footer .brand-name{color:var(--white);font-size:26px}
.site-footer .brand-mark{width:28px;height:28px}
.f-col{position:absolute;top:40px;font-size:9px;line-height:1.9}
.f-col h5{color:var(--cyan);font-size:11px;font-weight:700;margin-bottom:8px;text-transform:uppercase}
.map{position:absolute;left:880px;top:40px;width:130px;height:110px;border-radius:6px;background:linear-gradient(135deg,#e6eaee,#c6d0d8)}
.f-bar{position:absolute;left:0;bottom:0;width:1200px;height:40px;background:var(--sky);display:flex;justify-content:space-between;align-items:center;padding:0 190px 0 200px;font-size:9px}
.socials{display:flex;gap:8px}
.socials span{width:16px;height:16px;border-radius:50%;background:var(--white)}
</style>
</head>
<body>
<div class="page">
  <header class="site-header">
    <div class="brand"><div class="brand-mark"></div><div><div class="brand-name">KESTRAVO</div><div class="brand-sub">The Amber Horizon Company</div></div></div>
    <nav class="nav"><a class="active" href="#">HOME</a><a href="#">ABOUT US</a><a href="#">WHY CHOOSE US</a><a href="#">SERVICES</a><a href="#">CONTACT US</a><span class="dot"></span><span class="dot"></span></nav>
  </header>

  <section class="hero">
    <div class="hero-photo" role="img" aria-label="Aerial view of a container ship at a port"></div>
    <div class="hero-panel">
      <h1>Innovative Solutions for Maritime Security and Defense</h1>
      <p>Empowering Organizations With Cutting-Edge Consulting And Technology</p>
      <div class="tag">Where Innovation Meets Proficiency</div>
    </div>
  </section>

  <section class="about">
    <div class="about-text">
      <h2 class="section">About Us</h2>
      <p>KESTRAVO specializes in delivering innovative solutions for maritime security and defense in the fields of digital transformation and cybersecurity.</p>
      <p>By combining unparalleled expertise with strategic partnerships, we empower organizations to overcome challenges, seize opportunities and achieve success.</p>
      <span class="btn">Consult Now</span>
    </div>
    <div class="about-photo" role="img" aria-label="Naval warship at sea"></div>
  </section>

  <section class="services">
    <h2 class="section">Our Services</h2>
    <div class="svc-photo" role="img" aria-label="Surveillance drone flying over a city at dusk"></div>
    <div class="strategy">
      <h3>Strategy and Design</h3>
      <p>We help you build a clear path from vision to action, aligning your goals with practical, secure and modern solutions.</p>
      <div class="item"><div class="ico"><svg width="16" height="16" viewBox="0 0 16 16"><circle cx="7" cy="7" r="5" fill="none" stroke="#fff" stroke-width="2"/><path d="M11 11l4 4" stroke="#fff" stroke-width="2"/></svg></div><div><h4>Strategic Assessment</h4><p>Evaluating market savvy, identifying challenges and uncovering opportunities.</p></div></div>
      <div class="item"><div class="ico"><svg width="16" height="16" viewBox="0 0 16 16"><path d="M2 13l4-5 3 3 5-7" fill="none" stroke="#fff" stroke-width="2"/></svg></div><div><h4>Strategic Roadmaps</h4><p>Developing high-level plans that outline the steps, priorities and resources needed to achieve the organization's vision.</p></div></div>
      <div class="item"><div class="ico"><svg width="16" height="16" viewBox="0 0 16 16"><rect x="2" y="2" width="12" height="12" rx="2" fill="none" stroke="#fff" stroke-width="2"/><path d="M5 8l2 2 4-4" fill="none" stroke="#fff" stroke-width="2"/></svg></div><div><h4>Solution Design</h4><p>Crafting tailored, innovative and feasible solutions.</p></div></div>
    </div>
    <div class="exec">
      <h3>Execution and Delivery</h3>
      <p>Turning strategy into results through funding support, partnerships, acquisition and careful project management.</p>
      <div class="steps">
        <div class="step"><div class="ico"><svg width="22" height="22" viewBox="0 0 22 22"><circle cx="11" cy="11" r="8" fill="none" stroke="#0d3245" stroke-width="2"/><path d="M11 6v10M8 9h5" stroke="#0d3245" stroke-width="2"/></svg></div><h4>Funding Assistance</h4><p>Identifying funding opportunities and designing proposals.</p></div>
        <div class="step"><div class="ico"><svg width="22" height="22" viewBox="0 0 22 22"><circle cx="7" cy="8" r="3" fill="#0d3245"/><circle cx="15" cy="8" r="3" fill="#0d3245"/><path d="M2 18c1-4 9-4 10 0M10 18c1-4 9-4 10 0" fill="none" stroke="#0d3245" stroke-width="2"/></svg></div><h4>Partnership Development</h4><p>Identifying funding opportunities and designing proposals.</p></div>
        <div class="step"><div class="ico"><svg width="22" height="22" viewBox="0 0 22 22"><path d="M4 12l5 5 9-11" fill="none" stroke="#0d3245" stroke-width="2.5"/></svg></div><h4>Acquisition Support</h4><p>Defining requirements and assessing offers to ensure the best fit.</p></div>
        <div class="step"><div class="ico"><svg width="22" height="22" viewBox="0 0 22 22"><rect x="4" y="4" width="14" height="15" rx="2" fill="none" stroke="#0d3245" stroke-width="2"/><path d="M7 9h8M7 13h8" stroke="#0d3245" stroke-width="2"/></svg></div><h4>Project Management</h4><p>Delivering projects on schedule and within budget while ensuring quality.</p></div>
      </div>
      <span class="btn">Consult Now</span>
    </div>
  </section>

  <section class="why">
    <h2 class="section">Why Choose Us</h2>
    <div class="why-text">
      <h3>Expert Team</h3>
      <p class="lead">Decades of combined worldwide experience in maritime security, defense, digital transformation and cybersecurity, in public, private and research organizations, and in multidisciplinary teams.</p>
      <h4>Proven Partnerships</h4><p class="small">Access to state-of-the-art knowledge, practices and technology through key alliances.</p>
      <h4>Tailored Strategies</h4><p class="small">Customized designs addressing unique organizational needs.</p>
      <h4>Innovative Solutions</h4><p class="small">Leveraging cutting-edge technology and strategic insights.</p>
      <span class="btn">Consult Now</span>
    </div>
    <div class="why-photo" role="img" aria-label="Glowing digital padlock representing cybersecurity"></div>
  </section>

  <section class="collab">
    <h2 class="section">Let's Collaborate</h2>
    <div class="collab-photo" role="img" aria-label="Navy vessel moored in a harbour"></div>
    <div class="form">
      <h3>Ready to innovate together?</h3>
      <p>KESTRAVO is here to help you navigate challenges and unlock new opportunities for maritime security and defense with digital transformation and cybersecurity solutions.</p>
      <div class="row"><div class="field">First Name</div><div class="field">Last Name</div></div>
      <div class="row"><div class="field">Email</div><div class="field">Phone</div></div>
      <div class="field tall">Your Message</div>
      <span class="btn">Submit</span>
    </div>
  </section>

  <footer class="site-footer">
    <div class="brand"><div class="brand-mark"></div><div><div class="brand-name">KESTRAVO</div><div class="brand-sub">The Amber Horizon Company</div></div></div>
    <div class="f-col" style="left:560px"><h5>Contact Us</h5>+00 123 456 789<br>info@kestravo.com<br>12 Harbour Lane, Portside</div>
    <div class="f-col" style="left:760px"><h5>Quick Links</h5>Home<br>About Us<br>Why Choose Us<br>Services<br>Contact Us</div>
    <div class="map" role="img" aria-label="Location map"></div>
    <div class="f-bar"><span>© 2024 KESTRAVO. All Right Reserved</span><div class="socials"><span></span><span></span><span></span></div></div>
  </footer>
</div>
</body>
</html>
```